Visitenkarten-Design für Frauenarztpraxis
Zielgruppe
Frauenarztpraxis
Aufgabenstellung
auf der einen Seite Name (Dr. med. Brandl Susanne), auf der anderen Seite Fachärztin für Gynäkologie und Geburtshilfe, Lindengasse 27, 6158 Auwinkel, Tel. Nr. 05294/81305, Termine nach Vereinbarung

```html
<!DOCTYPE html>
<html lang="de">
<head>
<meta charset="utf-8">
<title>Visitenkarte – Dr. med. Brandl Susanne</title>
<link href="https://fonts.googleapis.com/css2?family=Fraunces:ital,opsz,wght@0,9..144,300;1,9..144,300&family=Josefin+Sans:ital,wght@0,600;1,300&family=Sacramento&display=swap" rel="stylesheet">
<style>
  :root {
    --backdrop: #546b59;
    --card: #f2f2f2;
    --ink: #1c1c1c;
    --ink-soft: #555555;
  }
  * { margin: 0; padding: 0; box-sizing: border-box; }
  html, body {
    width: 1200px;
    height: 800px;
    overflow: hidden;
    background: var(--backdrop);
  }
  .canvas {
    position: relative;
    width: 1200px;
    height: 800px;
  }
  .card {
    position: absolute;
    left: 388px;
    width: 404px;
    height: 231px;
    background: var(--card);
    color: var(--ink);
    text-align: center;
  }
  .card--front { top: 133px; }
  .card--back { top: 418px; }

  .card__title {
    position: absolute;
    top: 61px;
    width: 100%;
    font-family: "Josefin Sans", sans-serif;
    font-weight: 600;
    font-size: 11px;
    line-height: 14px;
    letter-spacing: 2.6px;
  }
  .card__name {
    position: absolute;
    top: 89px;
    width: 100%;
    font-family: "Sacramento", cursive;
    font-size: 46px;
    line-height: 56px;
    font-weight: 400;
  }

  .specialty {
    position: absolute;
    width: 100%;
    font-family: "Fraunces", serif;
    font-weight: 300;
    font-size: 19px;
    line-height: 24px;
    letter-spacing: 0.3px;
  }
  .specialty--first { top: 15px; }
  .specialty--second { top: 78px; }
  .specialty__amp {
    position: absolute;
    top: 40px;
    width: 100%;
    font-family: "Fraunces", serif;
    font-style: italic;
    font-weight: 300;
    font-size: 40px;
    line-height: 40px;
  }

  .contact {
    position: absolute;
    top: 130px;
    width: 100%;
    list-style: none;
    font-family: "Josefin Sans", sans-serif;
    font-style: italic;
    font-weight: 300;
    font-size: 10.5px;
    line-height: 18.5px;
    color: var(--ink-soft);
  }
  .appointments {
    position: absolute;
    top: 200px;
    width: 100%;
    font-family: "Josefin Sans", sans-serif;
    font-style: italic;
    font-weight: 300;
    font-size: 12.5px;
    line-height: 16px;
    letter-spacing: 0.3px;
  }
</style>
</head>
<body>
<main class="canvas">
  <section class="card card--front" aria-label="Vorderseite">
    <p class="card__title">DR. MED.</p>
    <h1 class="card__name">Brandl Susanne</h1>
  </section>

  <section class="card card--back" aria-label="Rückseite">
    <p class="specialty specialty--first">Fachärztin für Gynäkologie</p>
    <p class="specialty__amp">&amp;</p>
    <p class="specialty specialty--second">Geburtshilfe</p>
    <ul class="contact">
      <li>Lindengasse 27</li>
      <li>6158 Auwinkel</li>
      <li>+43 (0)5294 813 05</li>
    </ul>
    <p class="appointments">Termine nach Vereinbarung</p>
  </section>
</main>
</body>
</html>
```